International Automotive Parts Marketing business needs professional, sleek Android app design.

We have developed an Android app for our sales team and are now looking for an overall design our developers can apply. The design should mirror our corporate website kvrelo.com. There is a LOT of data the reps need to work through so not really any images other that login screen - of course icons are great. Lots of lists and searches etc. - it needs to look professional, feel amazing and easy to use. Our motto - Simple is always better. We included our logo and a few screenshots of the app page 1 and 2.

Target Market(s)

Professional Sales and Marketing - our own sales team (100 reps) will use this app

Font styles to use
Sans Serif

Colors

Designer to choose colors to be used in the design.

Requirements
Must have
• App design must be professional and easy to use in the field all day. Similar look and feel of corporate website kvrelo.com. Same colors and images. Icons to manage navigation
Should not have
• Non-professional look and feel. No vector cartoon type images. No specific parts related images

```html
<!DOCTYPE html>
<html lang="en">
<head>
<meta charset="utf-8">
<title>Kvrelo Parts – Sales App Screens</title>
<link href="https://fonts.googleapis.com/css2?family=Roboto:wght@400;500;700;900&display=swap" rel="stylesheet">
<style>
:root{
  --red:#b8203a;
  --red-dark:#951a2f;
  --ink:#222226;
  --muted:#9a9aa0;
  --line:#dedee2;
  --bg:#f3f3f5;
  --white:#ffffff;
  --scrim:rgba(20,20,22,.82);
  --ok:#3ccf5a;
}
*{box-sizing:border-box;margin:0;padding:0}
html,body{width:1200px;height:958px;overflow:hidden;background:var(--bg);font-family:"Roboto",Arial,sans-serif;color:var(--ink)}
.canvas{position:relative;width:1200px;height:958px}
.phone{position:absolute;width:210px;height:430px;background:var(--white);border-radius:16px;overflow:hidden;box-shadow:0 14px 30px rgba(120,20,40,.14),0 2px 6px rgba(0,0,0,.06);border-bottom:5px solid var(--red)}
.row1{top:30px}.row2{top:500px}
.c1{left:27px}.c2{left:261px}.c3{left:495px}.c4{left:729px}.c5{left:963px}
.r2c1{left:144px}.r2c2{left:378px}.r2c3{left:612px}.r2c4{left:846px}
.pad{padding:16px 16px 0}
.brand{display:flex;align-items:center;gap:6px}
.brand-dot{width:16px;height:16px;border-radius:50%;background:var(--red);flex:none}
.brand-name{font-size:13px;font-weight:900;color:var(--red);letter-spacing:.5px;text-transform:uppercase}
.topbar{display:flex;align-items:center;gap:12px;margin-bottom:12px}
.icon{width:14px;height:14px;flex:none}
.field{border-bottom:1px solid var(--line);padding:5px 0 4px;margin-bottom:8px}
.label{font-size:7px;color:var(--muted)}
.value{font-size:9px;font-weight:500}
.btn{display:block;text-align:center;background:var(--red);color:var(--white);font-size:9px;font-weight:700;border-radius:5px;padding:8px 0}
.btn-row{display:flex;gap:6px;margin:6px 0 12px}.btn-row .btn{flex:1}
.bottombar{position:absolute;left:0;right:0;bottom:0;height:30px;background:var(--red);display:flex;align-items:center;color:var(--white);font-size:8px;font-weight:700}
.bottombar span{flex:1;text-align:center;border-right:1px solid rgba(255,255,255,.3)}
.bottombar span:last-child{border:none}
.splash{display:flex;flex-direction:column;align-items:center;justify-content:center;height:100%}
.progress{width:120px;height:3px;background:var(--line);margin-top:18px;border-radius:2px}
.progress i{display:block;width:34%;height:100%;background:var(--ok);border-radius:2px}
.login{padding:70px 20px 0}
.login .brand{justify-content:center;margin-bottom:40px}
.login .field{margin-bottom:16px}
.link{display:block;text-align:center;font-size:8px;color:var(--red);text-decoration:underline;margin-top:10px}
.opt{display:flex;justify-content:space-between;align-items:center;font-size:8px;border-bottom:1px solid var(--line);padding:5px 0}
.opt .k{color:var(--muted)}
.box{width:9px;height:9px;border:1.2px solid var(--ink);border-radius:2px;display:inline-block}
.box.on{border-color:var(--red);background:var(--red)}
.section{font-size:9px;color:var(--muted);margin:4px 0 2px}
.drawer-head{background:var(--red);height:120px;padding:16px;color:var(--white);position:relative}
.drawer-head .brand-name{color:var(--white)}
.drawer-head .brand-dot{background:var(--white)}
.avatar{width:34px;height:34px;border-radius:50%;background:radial-gradient(circle at 40% 40%,#d9c2b4,#7b6a62);border:2px solid var(--white);position:absolute;left:16px;bottom:16px}
.who{position:absolute;left:58px;bottom:20px}
.who b{font-size:10px;display:block}
.who small{font-size:7px;opacity:.8}
.menu{padding:10px 16px}
.menu li{list-style:none;display:flex;align-items:center;gap:10px;font-size:9px;font-weight:500;padding:8px 0}
.menu li svg{width:11px;height:11px}
.logout{position:absolute;right:14px;bottom:14px;background:var(--red);color:var(--white);font-size:7px;font-weight:700;padding:5px 12px;border-radius:10px}
.dealer{display:flex;justify-content:space-between;align-items:flex-start;border-bottom:1px solid var(--line);padding:7px 0}
.dealer h4{font-size:7.5px;font-weight:700;text-transform:uppercase}
.dealer p{font-size:6.5px;color:var(--muted);margin-top:2px}
.dealer p em{color:var(--red);font-style:normal}
.pin{width:20px;height:20px;border-radius:50%;background:var(--red);display:flex;align-items:center;justify-content:center;flex:none}
.group{display:flex;justify-content:space-between;align-items:center;margin-bottom:4px}
.filter{width:20px;height:20px;border-radius:50%;background:var(--ink);display:flex;align-items:center;justify-content:center}
.title{font-size:8px;font-weight:700;text-transform:uppercase}
.sub{font-size:6.5px;color:var(--muted);margin-bottom:8px}
.big{font-size:10px;font-weight:700}
.scrim{position:absolute;inset:0;background:var(--scrim)}
.sheet{position:absolute;left:0;right:0;bottom:30px;background:var(--white);border-radius:22px 22px 0 0;padding:16px 20px 12px}
.sheet h5{font-size:12px;font-weight:500;color:var(--muted);margin-bottom:6px}
.sheet li{list-style:none;font-size:9px;font-weight:500;text-align:right;padding:6px 0;border-bottom:1px solid var(--line)}
.cancel{display:inline-block;background:var(--red);color:var(--white);font-size:7px;font-weight:700;padding:4px 12px;border-radius:9px;margin-top:8px}
.search-box{border:1px solid var(--red);border-radius:4px;padding:5px 7px;font-size:7px;color:var(--muted);display:flex;justify-content:space-between;margin-bottom:6px}
.supplier{display:flex;gap:8px;border-bottom:1px solid var(--line);padding:7px 0;font-size:6.5px}
.supplier .main{flex:1}
.supplier b{font-size:7.5px;display:block;margin-bottom:2px}
.supplier .side{text-align:right;color:var(--muted)}
.supplier .note{color:var(--muted);margin-top:2px}
.slider{display:flex;align-items:center;gap:6px;margin:6px 0}
.slider .lbl{font-size:7px;color:var(--muted);width:52px}
.track{flex:1;height:2px;background:var(--line);position:relative}
.track i{position:absolute;left:0;top:0;height:2px;background:var(--red)}
.track b{position:absolute;top:-3px;width:8px;height:8px;border-radius:50%;background:var(--red)}
.slider .num{font-size:8px;font-weight:700;color:var(--red);width:26px;text-align:right}
.toggle{width:24px;height:12px;border-radius:6px;background:var(--line);position:relative}
.toggle b{position:absolute;right:0;top:-1px;width:14px;height:14px;border-radius:50%;background:var(--red)}
.comment{background:#f1f1f3;height:54px;margin-top:8px;border-radius:4px;padding:6px;font-size:7px;color:var(--muted)}
.history{text-align:center;font-size:7px;color:var(--muted);margin-top:8px}
</style>
</head>
<body>
<div class="canvas">

  <!-- Splash -->
  <section class="phone row1 c1">
    <div class="splash">
      <div class="brand"><span class="brand-dot"></span><span class="brand-name">Kvrelo Parts</span></div>
      <div class="progress"><i></i></div>
    </div>
  </section>

  <!-- Login -->
  <section class="phone row1 c2">
    <div class="login">
      <div class="brand"><span class="brand-dot"></span><span class="brand-name">Kvrelo Parts</span></div>
      <div class="field"><div class="label">Username</div></div>
      <div class="field"><div class="label">Password</div></div>
      <a class="btn">Login</a>
      <a class="link">Forgot Password ?</a>
    </div>
  </section>

  <!-- Search -->
  <section class="phone row1 c3">
    <div class="pad">
      <div class="topbar">
        <svg class="icon" viewBox="0 0 14 14"><path d="M1 3h12M1 7h12M1 11h12" stroke="#222226" stroke-width="1.6"/></svg>
        <div class="brand"><span class="brand-dot"></span><span class="brand-name">Kvrelo Parts</span></div>
      </div>
      <div style="display:flex;gap:12px">
        <div class="field" style="flex:1"><div class="label">Type</div><div class="value">AB+M</div></div>
        <div class="field" style="flex:1"><div class="label">Rating</div><div class="value">ALL</div></div>
      </div>
      <div class="field"><div class="label">Please Enter Here</div></div>
      <a class="btn">Search</a>
      <div class="btn-row"><a class="btn">My Clients</a><a class="btn">Add Company</a></div>
      <div class="section">More Options</div>
      <div class="opt"><span class="k">Type</span><span>ALL</span></div>
      <div class="opt"><span class="k">Franchise</span><span>ALL</span></div>
      <div class="opt"><span class="k">LOI</span><span>None</span></div>
      <div class="opt"><span class="k">Rewards</span><span class="box on"></span></div>
      <div class="opt"><span class="k">My Touches</span><span class="box"></span></div>
      <div class="opt"><span class="k">Touch End</span><span>Pick a date</span></div>
      <div class="opt"><span class="k">Sale Type</span><span>Pick a date</span></div>
      <div class="opt"><span class="k">Sale Type</span><span>None</span></div>
    </div>
  </section>

  <!-- Dealer list -->
  <section class="phone row1 c4">
    <div class="pad">
      <div class="topbar">
        <svg class="icon" viewBox="0 0 14 14"><path d="M13 7H2M6 3 2 7l4 4" stroke="#222226" stroke-width="1.6" fill="none"/></svg>
        <div class="brand"><span class="brand-dot"></span><span class="brand-name">Kvrelo Parts</span></div>
      </div>
      <div class="group">
        <div class="field" style="width:110px;margin:0"><div class="label">Group by</div><div class="value">None</div></div>
        <span class="filter"><svg width="10" height="10" viewBox="0 0 10 10"><path d="M1 1h8L6 5v4L4 8V5z" fill="#fff"/></svg></span>
      </div>
      <div class="dealer"><div><h4>Halden Motor Group</h4><p>4810 Elm Ridge Rd, Dayton, USA</p><p>Last Touch <em>19 Jul 2019</em> · Type AB · Rating AB</p></div><span class="pin"><svg width="9" height="11" viewBox="0 0 9 11"><path d="M4.5 10S1 6.3 1 4a3.5 3.5 0 0 1 7 0c0 2.3-3.5 6-3.5 6z" fill="none" stroke="#fff" stroke-width="1.2"/></svg></span></div>
      <div class="dealer"><div><h4>Halden Motor Group</h4><p>4810 Elm Ridge Rd, Dayton, USA</p><p>Last Touch <em>19 Jul 2019</em> · Type AB · Rating AB</p></div><span class="pin"><svg width="9" height="11" viewBox="0 0 9 11"><path d="M4.5 10S1 6.3 1 4a3.5 3.5 0 0 1 7 0c0 2.3-3.5 6-3.5 6z" fill="none" stroke="#fff" stroke-width="1.2"/></svg></span></div>
      <div class="dealer"><div><h4>Halden Motor Group</h4><p>4810 Elm Ridge Rd, Dayton, USA</p><p>Last Touch <em>19 Jul 2019</em> · Type AB · Rating AB</p></div><span class="pin"><svg width="9" height="11" viewBox="0 0 9 11"><path d="M4.5 10S1 6.3 1 4a3.5 3.5 0 0 1 7 0c0 2.3-3.5 6-3.5 6z" fill="none" stroke="#fff" stroke-width="1.2"/></svg></span></div>
      <div class="dealer"><div><h4>Halden Motor Group</h4><p>4810 Elm Ridge Rd, Dayton, USA</p><p>Last Touch <em>19 Jul 2019</em> · Type AB · Rating AB</p></div><span class="pin"><svg width="9" height="11" viewBox="0 0 9 11"><path d="M4.5 10S1 6.3 1 4a3.5 3.5 0 0 1 7 0c0 2.3-3.5 6-3.5 6z" fill="none" stroke="#fff" stroke-width="1.2"/></svg></span></div>
      <div class="dealer"><div><h4>Halden Motor Group</h4><p>4810 Elm Ridge Rd, Dayton, USA</p><p>Last Touch <em>19 Jul 2019</em> · Type AB · Rating AB</p></div><span class="pin"><svg width="9" height="11" viewBox="0 0 9 11"><path d="M4.5 10S1 6.3 1 4a3.5 3.5 0 0 1 7 0c0 2.3-3.5 6-3.5 6z" fill="none" stroke="#fff" stroke-width="1.2"/></svg></span></div>
    </div>
  </section>

  <!-- Dealer detail -->
  <section class="phone row1 c5">
    <div class="pad">
      <div class="topbar">
        <svg class="icon" viewBox="0 0 14 14"><path d="M13 7H2M6 3 2 7l4 4" stroke="#222226" stroke-width="1.6" fill="none"/></svg>
        <div class="brand"><span class="brand-dot"></span><span class="brand-name">Kvrelo Parts</span></div>
      </div>
      <div class="title">Halden Motor Group</div>
      <div class="sub">4810 Elm Ridge Rd, Dayton, USA</div>
      <div class="field"><div class="label">Phone Number</div><div class="big">(555) 201-4531</div></div>
      <div class="field"><div class="label">Fax Number</div><div class="big">(555) 201-4598</div></div>
      <div class="field"><div class="label">Type</div><div class="big">M</div></div>
      <div class="field"><div class="label">Ratings</div><div class="big">B</div></div>
      <div class="field"><div class="label">Email Address</div><div class="big">sam.porter@northlaneauto.com</div></div>
      <div class="field"><div class="label">Comments</div><div class="big">Write Something Nice...</div></div>
      <div class="field"><div class="label">Partners</div><div class="big">MARLOW MOTORS</div></div>
      <div class="field"><div class="label">Franchise</div></div>
    </div>
    <div class="bottombar"><span>Edit</span><span>Modify List</span><span><svg width="12" height="8" viewBox="0 0 12 8" fill="#fff"><circle cx="2" cy="2" r="1"/><circle cx="6" cy="2" r="1"/><circle cx="10" cy="2" r="1"/><circle cx="2" cy="6" r="1"/><circle cx="6" cy="6" r="1"/><circle cx="10" cy="6" r="1"/></svg></span></div>
  </section>

  <!-- Record edit -->
  <section class="phone row2 r2c1">
    <div class="pad">
      <div class="topbar">
        <svg class="icon" viewBox="0 0 14 14"><path d="M13 7H2M6 3 2 7l4 4" stroke="#222226" stroke-width="1.6" fill="none"/></svg>
        <div class="brand"><span class="brand-dot"></span><span class="brand-name">Kvrelo Parts</span></div>
      </div>
      <div class="opt"><span class="k">Contact <u style="color:var(--ink)">Alex Parts Buyer</u></span><span>23 Oct 2019</span></div>
      <div class="opt"><span class="k">Type : OEM Parts NORDIX</span><span>City : Vancouver</span></div>
      <div class="opt"><span class="k">Franchise : NORDIX</span><span></span></div>
      <div class="slider"><span class="lbl">Discount (%)</span><span class="track"><i style="width:30%"></i><b style="left:28%"></b></span><span class="num">15</span></div>
      <div class="slider"><span class="lbl">Level</span><span class="track"><i style="width:45%"></i><b style="left:43%"></b></span><span class="num">04</span></div>
      <div class="slider"><span class="lbl">Monthly Vol ($)</span><span class="track"><i style="width:60%"></i><b style="left:58%"></b></span><span class="num">10000</span></div>
      <div class="opt"><span class="k">Clear This Record</span><span class="toggle"><b></b></span></div>
      <div class="opt"><span class="k">Simple note</span><span></span></div>
      <div class="comment">Here is the comments for a client...</div>
      <div class="history">Show History<br>•••</div>
    </div>
    <div class="bottombar"><span><svg width="12" height="12" viewBox="0 0 12 12"><path d="M2 10h8M3 8l5-6 2 2-5 6H3z" fill="none" stroke="#fff" stroke-width="1.1"/></svg></span><span>Comments</span><span>Save All</span></div>
  </section>

  <!-- Navigation drawer -->
  <section class="phone row2 r2c2">
    <div class="drawer-head">
      <div class="brand"><span class="brand-dot"></span><span class="brand-name">Kvrelo Parts</span></div>
      <span class="avatar" role="img" aria-label="Profile photo of the sales rep"></span>
      <div class="who"><b>Tomas Verek</b><small>Sales</small></div>
    </div>
    <ul class="menu">
      <li><svg viewBox="0 0 11 11"><rect x="1" y="2" width="9" height="8" fill="none" stroke="#b8203a"/><path d="M1 4h9" stroke="#b8203a"/></svg>Route</li>
      <li><svg viewBox="0 0 11 11"><circle cx="6" cy="5" r="3.2" fill="none" stroke="#b8203a"/><path d="M3.6 7.4 1 10" stroke="#b8203a"/></svg>Search</li>
      <li><svg viewBox="0 0 11 11"><path d="M1 2h1M4 2h6M1 5.5h1M4 5.5h6M1 9h1M4 9h6" stroke="#b8203a"/></svg>Custom List</li>
      <li><svg viewBox="0 0 11 11"><circle cx="5.5" cy="3.5" r="2.3" fill="none" stroke="#b8203a"/><path d="M1 10.5c0-2.5 2-4 4.5-4s4.5 1.5 4.5 4" fill="none" stroke="#b8203a"/></svg>Partner</li>
      <li><svg viewBox="0 0 11 11"><rect x="1" y="3" width="9" height="7" fill="none" stroke="#b8203a"/><path d="M4 3V1h3v2" fill="none" stroke="#b8203a"/></svg>Market Touches</li>
      <li><svg viewBox="0 0 11 11"><circle cx="5.5" cy="5.5" r="2" fill="none" stroke="#b8203a"/><circle cx="5.5" cy="5.5" r="4.3" fill="none" stroke="#b8203a" stroke-dasharray="2 1.4"/></svg>Settings</li>
    </ul>
    <span class="logout">Log out</span>
  </section>

  <!-- Supplier list -->
  <section class="phone row2 r2c3">
    <div class="pad">
      <div class="topbar">
        <svg class="icon" viewBox="0 0 14 14"><path d="M13 7H2M6 3 2 7l4 4" stroke="#222226" stroke-width="1.6" fill="none"/></svg>
        <div class="brand"><span class="brand-dot"></span><span class="brand-name">Kvrelo Parts</span></div>
      </div>
      <div class="search-box"><span>Search Shop Suppliers</span><span>☰</span></div>
      <div class="sub">Shop: Fairway Auto Service · Contact <u>Alex Parts Buyer</u></div>
      <div class="supplier"><span class="box on"></span><div class="main"><b>OEM Parts NORDIX</b>LOI : 01 · Disc(%) : 15<div class="note">23 Oct 2019 · Simple note</div></div><div class="side">Vancouver<br>Vol ($) : 15<br>Lakeside Nordix</div></div>
      <div class="supplier"><span class="box"></span><div class="main"><b>OEM Parts NORDIX</b>LOI : 01 · Disc(%) : 15<div class="note">23 Oct 2019 · Simple note</div></div><div class="side">Vancouver<br>Vol ($) : 15<br>Lakeside Nordix</div></div>
      <div class="supplier"><span class="box"></span><div class="main"><b>OEM Parts NORDIX</b>LOI : 01 · Disc(%) : 15<div class="note">23 Oct 2019 · Simple note</div></div><div class="side">Vancouver<br>Vol ($) : 15<br>Lakeside Nordix</div></div>
      <div class="supplier"><span class="box"></span><div class="main"><b>OEM Parts NORDIX</b>LOI : 01 · Disc(%) : 15<div class="note">23 Oct 2019 · Simple note</div></div><div class="side">Vancouver<br>Vol ($) : 15<br>Lakeside Nordix</div></div>
    </div>
    <div class="bottombar"><span><svg width="12" height="12" viewBox="0 0 12 12"><path d="M2 10h8M3 8l5-6 2 2-5 6H3z" fill="none" stroke="#fff" stroke-width="1.1"/></svg></span><span>Comments</span><span>Send Action Alert</span></div>
  </section>

  <!-- Detail with action sheet -->
  <section class="phone row2 r2c4">
    <div class="pad">
      <div class="topbar">
        <svg class="icon" viewBox="0 0 14 14"><path d="M13 7H2M6 3 2 7l4 4" stroke="#222226" stroke-width="1.6" fill="none"/></svg>
        <div class="brand"><span class="brand-dot"></span><span class="brand-name">Kvrelo Parts</span></div>
      </div>
      <div class="title">Halden Motor Group</div>
      <div class="sub">4810 Elm Ridge Rd, Dayton, USA</div>
      <div class="field"><div class="label">Phone Number</div><div class="big">(555) 201-4531</div></div>
      <div class="field"><div class="label">Fax Number</div><div class="big">(555) 201-4598</div></div>
      <div class="field"><div class="label">Type</div><div class="big">M</div></div>
      <div class="field"><div class="label">Ratings</div><div class="big">B</div></div>
    </div>
    <div class="scrim"></div>
    <div class="sheet">
      <h5>Choose One</h5>
      <ul><li>Contacts</li><li>Touches</li><li>Alerts</li><li>Rewards</li><li>Supplier</li></ul>
      <div style="text-align:right"><span class="cancel">Cancel</span></div>
    </div>
    <div class="bottombar"><span>Edit</span><span>Modify List</span><span><svg width="12" height="8" viewBox="0 0 12 8" fill="#fff"><circle cx="2" cy="2" r="1"/><circle cx="6" cy="2" r="1"/><circle cx="10" cy="2" r="1"/><circle cx="2" cy="6" r="1"/><circle cx="6" cy="6" r="1"/><circle cx="10" cy="6" r="1"/></svg></span></div>
  </section>

</div>
</body>
</html>
```